vQTA Company brochure For sales and Marketing

WE need a brochure design for our company called vQTA. The logo is gold. This is an Airline Maintenace Software Company. The software it is called vQTA.

We will like the Brochure to include our modules and a brief description on what they are about.

The front cover we want to have purple night sky screen. With our logo and out motto.

The first page can have the company bio. And the inside the Company modules description.

the back can have contact Sales information.

We will like this to be modern and with style. Ower mention Perlotti catalog.

please see out sample Web Site

http://kdaran52.sitepadhub.com/vqta

Target Market(s)

Airlines

Industry/Entity Type

Airline

Requirements
Must have
• gold, black , purple, grey and chrome. we like mature scenes or night sky
Nice to have

```html
<!DOCTYPE html>
<html lang="en">
<head>
<meta charset="utf-8">
<title>vQTA Brochure – Module Spread</title>
<link rel="stylesheet" href="https://fonts.googleapis.com/css2?family=Open+Sans:wght@400;700;800&display=swap">
<style>
  :root {
    --backdrop: #cfcfcf;
    --purple-light: #4a2a78;
    --purple: #33195a;
    --purple-deep: #1c0c36;
    --black-light: #3a3a40;
    --black: #222226;
    --black-deep: #0e0e10;
    --gold: #d8b25a;
    --gold-light: #f0d28a;
    --chrome: #c9ccd3;
    --ink: #ffffff;
    --ink-soft: rgba(236,236,242,0.88);
    --band-chrome: rgba(201,204,211,0.22);
    --band-gold: rgba(216,178,90,0.28);
    --screen-dark: #2c2f36;
    --screen-blue: #1d4f9c;
    --screen-light: #eef2f7;
  }
  * { box-sizing: border-box; margin: 0; padding: 0; }
  html, body { width: 1200px; height: 900px; overflow: hidden; }
  body {
    background: var(--backdrop);
    font-family: "Open Sans", Arial, sans-serif;
    display: flex; align-items: center; justify-content: center;
  }
  .spread {
    width: 1040px; height: 700px;
    display: flex;
    box-shadow: 0 18px 40px rgba(0,0,0,0.28);
  }
  .page { position: relative; width: 520px; height: 700px; overflow: hidden; color: var(--ink); }
  .page--purple { background: linear-gradient(160deg, var(--purple-light), var(--purple) 50%, var(--purple-deep)); }
  .page--black { background: linear-gradient(160deg, var(--black-light), var(--black) 45%, var(--black-deep)); }
  .page-bands { position: absolute; inset: 0; width: 100%; height: 100%; }
  .module { position: absolute; }
  .module h2 {
    font-size: 12px; font-weight: 800; text-transform: uppercase;
    letter-spacing: 0.2px; margin-bottom: 6px; line-height: 1.3;
    color: var(--gold);
  }
  .module p { font-size: 9.6px; line-height: 1.42; color: var(--ink-soft); }

  .screen {
    position: absolute; width: 200px; height: 128px;
    border: 3px solid var(--chrome);
    background: linear-gradient(90deg, var(--screen-dark) 0 14%, var(--screen-light) 14% 100%);
    box-shadow: 0 4px 12px rgba(0,0,0,0.45);
  }
  .screen::before {
    content: ""; position: absolute; left: 14%; right: 0; top: 0; height: 14px;
    background: var(--screen-blue);
  }
  .tablet {
    position: absolute; left: 38px; top: 305px; width: 150px; height: 210px;
    border: 5px solid #111; border-radius: 6px;
    outline: 1px solid var(--chrome);
    background: linear-gradient(180deg, #c9d8e6 0%, #8eaecb 45%, #3e6a93 80%, #2b4e72 100%);
    box-shadow: 0 6px 16px rgba(0,0,0,0.5);
  }
</style>
</head>
<body>
<main class="spread">

  <section class="page page--purple" aria-label="Modules, left page">
    <svg class="page-bands" viewBox="0 0 520 700" preserveAspectRatio="none" aria-hidden="true">
      <path d="M0 215 Q260 185 520 230 L520 244 Q260 199 0 229 Z" fill="var(--band-chrome)"/>
      <path d="M0 450 Q260 420 520 465 L520 479 Q260 434 0 464 Z" fill="var(--band-gold)"/>
    </svg>

    <div class="screen" style="left:24px; top:40px;" role="img" aria-label="Planning module software screen"></div>
    <article class="module" style="left:240px; top:34px; width:260px;">
      <h2>The Planning Module</h2>
      <p>The highly efficient Planning module allows for interrogation of all available items within the system – from aircraft down to component level. Forecasting by flight hours, cycles and calendar limits is presented in one view, and work packages can be built, released and tracked from here. Short, medium and long term planning are all catered for within the module.</p>
    </article>

    <div class="screen" style="left:24px; top:272px;" role="img" aria-label="Technical records module screen with aircraft seat layout"></div>
    <article class="module" style="left:240px; top:262px; width:260px;">
      <h2>The Technical Records Module</h2>
      <p>Implementing lean processes and reducing costs are an operator's foremost concerns. The Technical Records module allows the user to record all associated aircraft, engine and component information. Status reports, MEL deferrals and airworthiness directives are monitored in real time, and full configuration control can be maintained within the system.</p>
    </article>

    <div class="screen" style="left:24px; top:505px;" role="img" aria-label="Reliability module screen with charts"></div>
    <article class="module" style="left:240px; top:497px; width:260px;">
      <h2>The Reliability Module</h2>
      <p>Management and Aviation Authority requirements can be met by the collection of reliability information directly from the system, without the need for additional software packages. Using data from defects, removals and delays, the module provides alerts, reports and graphs, enabling them to give you faster and more accurate feedback.</p>
    </article>
  </section>

  <section class="page page--black" aria-label="Modules, right page">
    <svg class="page-bands" viewBox="0 0 520 700" preserveAspectRatio="none" aria-hidden="true">
      <path d="M0 240 L520 0 L520 250 L0 470 Z" fill="rgba(201,204,211,0.06)"/>
      <path d="M0 262 Q260 245 520 262 L520 270 Q260 253 0 270 Z" fill="var(--band-chrome)"/>
      <path d="M0 520 Q260 500 520 520 L520 528 Q260 508 0 528 Z" fill="var(--band-gold)"/>
    </svg>

    <article class="module" style="left:28px; top:34px; width:220px;">
      <h2>The Production Control Module</h2>
      <p>Improving and maximizing productivity, along with cost savings, are the hallmarks of the vQTA Maintenance software. The Production Control module provides all of the functionality needed to effectively prepare, issue and close work orders. Labor, parts and tooling are tracked against each task, and electronic signatures allow digital sign-off for maintenance on aircraft and components.</p>
    </article>
    <article class="module" style="left:272px; top:34px; width:225px;">
      <h2>The Shop Module</h2>
      <p>The Shop module, which focuses primarily on component repair and overhaul, allows in-house and third party maintenance to be controlled from one place. Work orders, parts and labor are recorded against each component, and the shop can be managed as a workshop in its own right. Electronic signature is also available for the sign-off of work on components.</p>
    </article>

    <div class="tablet" role="img" aria-label="Tablet showing the mobile app login over a view of an aircraft wing above the clouds"></div>
    <article class="module" style="left:220px; top:320px; width:270px;">
      <h2>vQTA M</h2>
      <p>The vQTA mobile module (vQTAM) allows you to stay connected wherever you are, whether in the office, on the hangar floor or out on the line. Access aircraft information, review tasks and sign off work from your mobile device, giving your team the mobility to work anywhere while remaining fully integrated with the system, streamlining your processes.</p>
    </article>

    <article class="module" style="left:28px; top:555px; width:220px;">
      <h2>The Library Module</h2>
      <p>The comprehensive Library module provides the necessary capability to effectively monitor all technical manuals and documentation within your organization. A workflow system allows for the control of revisions, with full revision history, and notifications with the Read &amp; Sign feature.</p>
    </article>
    <article class="module" style="left:272px; top:555px; width:225px;">
      <h2>The Quality Assurance Module</h2>
      <p>The Quality Assurance module is an effective internal and external audit program that will bring benefits beyond regulatory compliance. Audits, findings and corrective actions are tracked to closure, supplier approvals are controlled, and audit tracking helps maintain compliance to regulatory requirements.</p>
    </article>
  </section>

</main>
</body>
</html>
```